billboard campaign Meridale Flyers Guild

We want to run a targeted billboard campaign during the Harvest Cup in Las Vegas. The Meridale Flyers Guild is in prolonged contract negotiations with management. We want to bring public attention to our negotiations and pressure on the company to negotiate more quickly. Meridale Air owns the naming rights to "Meridale Stadium" in vegas where the harvest cup will be held. We would like artwork for this campaign that will be displayed on multiple billboards around the stadium and las vegas strip, and are seeking help in its design.
We would like to use a word play on the phrase "Big Game" which is frequently used as a alternative in advertising in reference to the Harvest Cup. Our initial thought was a simple billboard incorporating our colors and with our logo saying " Our Contract, Is Not a Big Game!" or "Meridale Flyer's Futures Are Not A Big Game!" But we are open to other suggestions and slogans. In the past we have used some artwork for picketing event which I will include for reference for logo and color scheme. The Local 4637 Haulworkers logo and union name must appear in the artwork. "Meridale Flyers Guild Haulworkers Local 4637"

Target Market(s)

Harvest Cup Attendees, Las Vegas tourists

Industry/Entity Type

aviation, labor union

Colors

Designer to choose colors to be used in the design.

Requirements
Must have
• The colors of the union logo must be those used in the included pdf art examples.

```html
<!DOCTYPE html>
<html lang="en">
<head>
<meta charset="utf-8">
<title>Our Contract Is Not A Big Game – Meridale Flyers Guild</title>
<link href="https://fonts.googleapis.com/css2?family=Bebas+Neue&family=Archivo+Black&display=swap" rel="stylesheet">
<style>
  :root {
    --union-navy: #23386f;
    --union-gold: #f5b71a;
    --panel-white: #ffffff;
  }
  html, body {
    margin: 0;
    padding: 0;
    width: 1200px;
    height: 3599px;
    overflow: hidden;
    background: var(--union-gold);
  }
  .billboard {
    display: block;
    width: 1200px;
    height: 3599px;
  }
  .headline {
    font-family: "Bebas Neue", "Oswald", sans-serif;
  }
  .ink-navy { fill: var(--union-navy); }
  .ink-gold { fill: var(--union-gold); }
  .union-mark-name {
    font-family: "Bebas Neue", "Oswald", sans-serif;
    fill: var(--union-navy);
  }
  .signature {
    font-family: "Archivo Black", "Arial Black", sans-serif;
    fill: var(--union-navy);
  }
</style>
</head>
<body>
<svg class="billboard" viewBox="0 0 1200 3599" xmlns="http://www.w3.org/2000/svg">
  <!-- Frame and panel -->
  <rect class="frame" x="0" y="0" width="1200" height="3599" fill="var(--union-gold)"/>
  <rect class="panel" x="98" y="87" width="1004" height="3420" fill="var(--panel-white)"/>
  <path class="panel-wave-base" d="M0 3465 C 250 3340, 500 3345, 720 3390 S 1050 3405, 1200 3345 L 1200 3599 L 0 3599 Z" fill="var(--union-gold)"/>
  <path class="panel-wave-line" d="M0 3465 C 250 3340, 500 3345, 720 3390 S 1050 3405, 1200 3345" fill="none" stroke="var(--union-navy)" stroke-width="13"/>

  <!-- Headline -->
  <g class="headline">
    <text class="ink-navy" x="151" y="733" font-size="819" textLength="876" lengthAdjust="spacingAndGlyphs">OUR</text>
    <text class="ink-gold" x="151" y="1048" font-size="360" textLength="886" lengthAdjust="spacingAndGlyphs">CONTRACT,</text>
    <text class="ink-navy" x="151" y="1453" font-size="470" textLength="876" lengthAdjust="spacingAndGlyphs">IS NOT A</text>
    <text class="ink-gold" x="151" y="2089" font-size="789" textLength="897" lengthAdjust="spacingAndGlyphs">BIG</text>
    <text class="ink-navy" x="151" y="2508" font-size="530" textLength="897" lengthAdjust="spacingAndGlyphs">GAME!</text>
  </g>

  <!-- Union mark -->
  <g class="union-mark">
    <circle cx="600" cy="2790" r="150" fill="var(--union-navy)"/>
    <text class="union-mark-name" x="600" y="3080" font-size="96" text-anchor="middle">HAULWORKERS LOCAL 4637</text>
  </g>

  <!-- Union signature -->
  <g class="signature">
    <text x="120" y="3205" font-size="84" textLength="961" lengthAdjust="spacingAndGlyphs">Meridale Flyers Guild</text>
    <text x="120" y="3305" font-size="118" textLength="961" lengthAdjust="spacingAndGlyphs">Haulworkers Local 4637</text>
  </g>
</svg>
</body>
</html>
```